Business Card Design

I'd like to have some business cards designed using my new logo. I am an accountant and company secretary and offer these services through Holloway Meridian Advisory Pty Ltd. I am the sole Director of the company. Please let me know if you require any further logo files.

Industry/Entity Type

Business

```html
<!DOCTYPE html>
<html lang="en">
<head>
<meta charset="utf-8">
<title>Holloway Meridian Advisory – Business Card</title>
<link rel="stylesheet" href="https://fonts.googleapis.com/css2?family=EB+Garamond:ital,wght@0,400;1,400&family=Share+Tech+Mono&display=swap">
<style>
  :root {
    --ink: #0b0b0d;
    --rule: #6b6f74;
    --brand-grey: #5d6670;
    --brand-dot: #2a8fd6;
    --sky-white: #ffffff;
    --sky-pale: #d8f3f7;
    --sky-aqua: #6fd6ec;
    --sky-blue: #1fa6e6;
    --sky-deep: #0a5fd6;
    --city-violet: #a78ad8;
    --city-cyan: #8fe3ee;
  }
  * { box-sizing: border-box; margin: 0; padding: 0; }
  html, body { width: 1200px; height: 741px; overflow: hidden; background: #ffffff; }

  .card {
    position: relative;
    width: 1200px;
    height: 741px;
    overflow: hidden;
    background:
      radial-gradient(ellipse 520px 260px at 180px 120px, rgba(255,255,255,0.95), rgba(255,255,255,0) 70%),
      radial-gradient(ellipse 420px 380px at 200px 430px, rgba(255,255,255,0.9), rgba(255,255,255,0) 75%),
      radial-gradient(ellipse 360px 140px at 1140px 290px, rgba(10,95,214,0.9), rgba(10,95,214,0) 80%),
      radial-gradient(ellipse 500px 200px at 1100px 560px, rgba(31,166,230,0.7), rgba(31,166,230,0) 80%),
      linear-gradient(180deg, var(--sky-pale) 0%, var(--sky-white) 14%, var(--sky-pale) 26%, var(--sky-aqua) 44%, #8fe0ef 62%, var(--sky-aqua) 78%, var(--sky-blue) 100%),
      var(--sky-aqua);
  }

  .brand {
    position: absolute;
    left: 28px;
    top: 38px;
    display: flex;
    align-items: center;
    gap: 26px;
  }
  .brand__dot {
    width: 62px;
    height: 62px;
    border-radius: 50%;
    background: var(--brand-dot);
    flex: none;
  }
  .brand__name {
    font-family: "EB Garamond", Georgia, serif;
    font-weight: 400;
    font-size: 25px;
    line-height: 28px;
    color: var(--brand-grey);
    letter-spacing: 0.5px;
    text-transform: uppercase;
  }

  .company {
    position: absolute;
    right: 62px;
    top: 124px;
    text-align: right;
  }
  .company__name,
  .company__reflection {
    font-family: "Share Tech Mono", "Courier New", monospace;
    font-size: 42px;
    font-weight: 700;
    letter-spacing: 3px;
    color: var(--ink);
    line-height: 44px;
    white-space: nowrap;
  }
  .company__reflection {
    transform: scaleY(-0.8);
    transform-origin: top;
    margin-top: 2px;
    opacity: 0.18;
    filter: blur(1px);
    height: 30px;
  }
  .company__slogan {
    position: absolute;
    left: 640px;
    width: 420px;
    top: 200px;
    text-align: center;
    font-family: "EB Garamond", Georgia, serif;
    font-style: italic;
    font-size: 37px;
    color: var(--ink);
  }

  .person {
    position: absolute;
    left: 640px;
    width: 418px;
    top: 328px;
    text-align: center;
  }
  .person__name {
    font-family: "Share Tech Mono", "Courier New", monospace;
    font-weight: 700;
    font-size: 42px;
    letter-spacing: 3px;
    color: var(--ink);
    line-height: 46px;
    padding-bottom: 4px;
    border-bottom: 4px solid var(--rule);
  }
  .person__role {
    font-family: "EB Garamond", Georgia, serif;
    font-style: italic;
    font-size: 33px;
    color: var(--ink);
    margin-top: 2px;
  }

  .contact {
    position: absolute;
    left: 639px;
    top: 472px;
    font-family: "Share Tech Mono", "Courier New", monospace;
    font-weight: 700;
    font-size: 30px;
    letter-spacing: 1.5px;
    color: var(--ink);
    line-height: 38.8px;
    font-style: normal;
  }
  .contact__row { display: flex; white-space: nowrap; }
  .contact__label { width: 207px; }

  .skyline {
    position: absolute;
    left: 0;
    top: 480px;
    width: 600px;
    height: 261px;
    background:
      linear-gradient(180deg, rgba(255,255,255,0) 0%, rgba(255,255,255,0.3) 100%),
      linear-gradient(90deg, var(--city-violet) 0%, var(--city-cyan) 45%, rgba(143,227,238,0.6) 70%, rgba(143,227,238,0) 100%);
    -webkit-mask-image: linear-gradient(180deg, transparent 0%, #000 30%, #000 85%, transparent 100%);
    mask-image: linear-gradient(180deg, transparent 0%, #000 30%, #000 85%, transparent 100%);
    opacity: 0.75;
  }
</style>
</head>
<body>
  <main class="card">
    <div class="skyline" role="img" aria-label="Photograph of a city skyline on the waterfront"></div>

    <header class="brand">
      <span class="brand__dot" aria-hidden="true"></span>
      <p class="brand__name">Holloway<br>Meridian Advisory<br>Pty Ltd</p>
    </header>

    <section class="company">
      <h1 class="company__name">FULL NAME OF COMPANY</h1>
      <div class="company__reflection" aria-hidden="true">FULL NAME OF COMPANY</div>
    </section>
    <p class="company__slogan">Slogan Company</p>

    <section class="person">
      <h2 class="person__name">NAME LAST NAME</h2>
      <p class="person__role">Position</p>
    </section>

    <address class="contact">
      <div class="contact__row">Adress Street Name</div>
      <div class="contact__row">City Country Postal</div>
      <div class="contact__row"><span class="contact__label">Phone</span><span>+000 00</span></div>
      <div class="contact__row"><span class="contact__label">Mobile</span><span>+000 00</span></div>
      <div class="contact__row"><span class="contact__label">Fax</span><span>+000 00</span></div>
    </address>
  </main>
</body>
</html>
```